Design business card for new business which advocates for elders in nursing homes or personal care h

New business for rights of the elderly residents who reside in personal care homes and or nursing homes. I am looking for a business card with logo of keystone for Pennsylvania and something in side the keystone that represents healthcare, advocates, something on that line; monitor care received and needs of resident. Chart audits, State Regulation compliance

Target Market(s)

Seniors no longer safe to live at home by themselves along with their kids

Industry/Entity Type

Business

Contact Information for Business Card

Keystone symbol to represent Pensylvaoa with some kind of symbol inside to represent advocate, seniors, or healthcare symbol

Font styles to use
Serif

Colors
33a6d7
85cae6
abd037

Requirements
Must have
• Brightwell Elder Allies is our business name; our tag line is Path to Better Living
Nice to have
• Nice logo

```html
<!DOCTYPE html>
<html lang="en">
<head>
<meta charset="utf-8">
<title>Brightwell Elder Allies – Business Card</title>
<link rel="stylesheet" href="https://fonts.googleapis.com/css2?family=Tinos:wght@400;700&display=swap">
<style>
  :root {
    --sky: #33a6d7;
    --sky-light: #85cae6;
    --sky-deep: #2a8fc0;
    --ink: #1c1c1c;
    --ink-soft: #3a3a3a;
    --paper: #ffffff;
    --paper-shade: #eef0f1;
    --stage: #e7e4df;
  }
  * { margin: 0; padding: 0; box-sizing: border-box; }
  html, body { width: 1200px; height: 885px; overflow: hidden; }
  body {
    background: var(--stage);
    font-family: "Tinos", "Times New Roman", serif;
    color: var(--ink);
    position: relative;
  }
  .card {
    position: absolute;
    width: 540px;
    height: 309px;
    border-radius: 16px;
    box-shadow: 0 6px 18px rgba(0,0,0,0.18);
    overflow: hidden;
  }
  /* Front */
  .card--front {
    left: 50px; top: 130px;
    background: linear-gradient(135deg, var(--paper) 55%, var(--paper-shade));
  }
  .brand {
    position: absolute;
    left: 34px; top: 40px;
    display: flex; align-items: center; gap: 14px;
  }
  .brand__mark {
    width: 58px; height: 58px;
    background: var(--sky);
    flex: none;
  }
  .brand__name {
    font-weight: 700;
    font-size: 24px;
    line-height: 1.05;
    text-transform: uppercase;
    letter-spacing: 0.5px;
    color: var(--ink);
  }
  .brand__tagline {
    font-size: 10px;
    letter-spacing: 3px;
    color: var(--ink-soft);
    margin-top: 6px;
  }
  .person {
    position: absolute;
    right: 34px; top: 118px;
    text-align: right;
  }
  .person__name { font-size: 22px; color: var(--ink); }
  .person__role { font-size: 13px; color: var(--sky); margin-top: 2px; }
  .divider {
    position: absolute;
    left: 34px; right: 150px; top: 176px;
    height: 1.5px;
    background: var(--sky);
  }
  .contacts {
    position: absolute;
    left: 34px; bottom: 28px;
    list-style: none;
  }
  .contacts li {
    display: flex; align-items: center; gap: 10px;
    font-size: 14px; color: var(--ink-soft);
    margin-top: 6px;
  }
  .contacts svg { width: 18px; height: 18px; flex: none; }
  .address {
    position: absolute;
    right: 34px; bottom: 30px;
    text-align: right;
    font-size: 14px; line-height: 1.45;
    color: var(--ink-soft);
  }
  /* Back */
  .card--back {
    left: 610px; top: 446px;
    background: linear-gradient(135deg, var(--sky-light) 0%, var(--sky) 45%, var(--sky-deep) 100%);
    display: flex; align-items: center; justify-content: center;
  }
  .back-brand { display: flex; align-items: center; gap: 16px; }
  .back-brand__mark { width: 70px; height: 70px; background: var(--paper); flex: none; }
  .back-brand__name {
    font-weight: 700; font-size: 28px; line-height: 1.05;
    text-transform: uppercase; letter-spacing: 0.5px;
    color: var(--paper);
  }
  .back-brand__tagline {
    font-size: 11px; letter-spacing: 3.5px;
    color: var(--paper); margin-top: 7px;
  }
</style>
</head>
<body>

<section class="card card--front">
  <div class="brand">
    <div class="brand__mark"></div>
    <div>
      <div class="brand__name">Brightwell<br>Elder Allies</div>
      <div class="brand__tagline">Path to Better Living</div>
    </div>
  </div>

  <div class="person">
    <div class="person__name">Employee Name</div>
    <div class="person__role">Managing Director</div>
  </div>

  <div class="divider"></div>

  <ul class="contacts">
    <li>
      <svg viewBox="0 0 18 18" aria-hidden="true"><rect width="18" height="18" fill="#33a6d7"/><path d="M6 4.5c.6 0 1 .3 1.2.8l.6 1.5c.1.4 0 .8-.3 1l-.7.6c.5 1 1.3 1.8 2.3 2.3l.6-.7c.3-.3.7-.4 1-.3l1.5.6c.5.2.8.6.8 1.2v.8c0 .7-.6 1.2-1.3 1.2C8 13.4 4.6 10 4.5 5.8c0-.7.5-1.3 1.2-1.3z" fill="#fff"/></svg>
      0047 2913 568
    </li>
    <li>
      <svg viewBox="0 0 18 18" aria-hidden="true"><rect width="18" height="18" fill="#33a6d7"/><rect x="4" y="5.5" width="10" height="7" fill="none" stroke="#fff" stroke-width="1.2"/><path d="M4 5.5l5 4 5-4" fill="none" stroke="#fff" stroke-width="1.2"/></svg>
      hello@brightwell.org
    </li>
    <li>
      <svg viewBox="0 0 18 18" aria-hidden="true"><rect width="18" height="18" fill="#33a6d7"/><circle cx="9" cy="9" r="5" fill="none" stroke="#fff" stroke-width="1.1"/><ellipse cx="9" cy="9" rx="2.2" ry="5" fill="none" stroke="#fff" stroke-width="1"/><path d="M4 9h10" stroke="#fff" stroke-width="1"/></svg>
      www.brightwell.org
    </li>
  </ul>

  <div class="address">Brightwell Office<br>14 Maple Row, PA 17052</div>
</section>

<section class="card card--back">
  <div class="back-brand">
    <div class="back-brand__mark"></div>
    <div>
      <div class="back-brand__name">Brightwell<br>Elder Allies</div>
      <div class="back-brand__tagline">Path to Better Living</div>
    </div>
  </div>
</section>

</body>
</html>
```